Letterhead design for business

Looking for an attractive and professional letterhead that uses the logo that is attached below.

Target Market(s)

Potential bankruptcy clients.

Industry/Entity Type

Legal

Colors

Designer to choose colors to be used in the design.

Requirements
Must have
• Address for locations, phone number, and website address.
• Addresses are on website larkmoorfirm.legal. Use following phone number (for tracking purposes): 404-731-2864

```html
<!DOCTYPE html>
<html lang="en">
<head>
<meta charset="utf-8">
<title>Larkmoor Law Group — Letterhead</title>
<link href="https://fonts.googleapis.com/css2?family=PT+Sans:wght@400;700&family=Arimo:wght@700&display=swap" rel="stylesheet">
<style>
  :root {
    --backdrop: #e4e4e4;
    --paper: #f8f8f7;
    --charcoal: #3a3a38;
    --leaf: #8cc07e;
    --ink: #4a4a4a;
    --heading: #1e1e1e;
    --light: #ffffff;
    --sig-tone: #d9d9d9;
  }
  * { margin: 0; padding: 0; box-sizing: border-box; }
  html, body { width: 1200px; height: 998px; overflow: hidden; }
  body { background: var(--backdrop); position: relative; font-family: "PT Sans", sans-serif; }
  .letterhead {
    position: absolute; left: 260px; top: 19px; width: 680px; height: 960px;
    background: var(--paper); box-shadow: 0 6px 22px rgba(0,0,0,.18);
    overflow: hidden;
  }
  .header-waves { position: absolute; left: 0; top: 0; width: 680px; height: 160px; }
  .brand {
    position: absolute; left: 58px; top: 88px; display: flex; align-items: center; gap: 10px;
    font-family: "PT Sans", sans-serif; font-weight: 700; font-size: 22px; color: var(--charcoal);
  }
  .brand-dot { width: 14px; height: 14px; border-radius: 50%; background: var(--leaf); }
  .brand-byline {
    position: absolute; left: 82px; top: 118px; font-size: 9px; color: var(--charcoal);
    letter-spacing: .5px;
  }
  .contact {
    position: absolute; left: 443px; top: 20px; color: var(--light); font-size: 10px; line-height: 15px;
  }
  .contact-line { display: flex; align-items: center; gap: 5px; }
  .contact-line svg { width: 8px; height: 8px; fill: var(--leaf); }
  .addresses {
    margin-top: 5px; padding-left: 10px; border-left: 1.5px solid var(--leaf);
  }
  .salutation {
    position: absolute; left: 61px; top: 195px;
    font-family: "Arimo", sans-serif; font-weight: 700; font-size: 14.5px; color: var(--heading);
  }
  .letter-body {
    position: absolute; left: 62px; top: 234px; width: 557px;
    font-size: 13.7px; line-height: 17.8px; color: var(--ink); text-align: justify;
  }
  .letter-body p { margin-bottom: 17.8px; }
  .signature {
    position: absolute; left: 62px; top: 700px; width: 106px; height: 52px;
    background: var(--sig-tone); border-radius: 4px;
  }
</style>
</head>
<body>
  <main class="letterhead">
    <svg class="header-waves" viewBox="0 0 767 180" preserveAspectRatio="none" aria-hidden="true">
      <path fill="var(--charcoal)" d="M0 0 H767 V155 C620 172 480 152 380 102 C300 62 180 12 0 14 Z"/>
      <path fill="var(--leaf)" d="M0 18 C180 16 300 66 380 106 C480 156 620 176 767 160 V168 C600 184 460 168 360 118 C280 78 170 40 0 44 Z"/>
      <path fill="var(--charcoal)" d="M0 72 C120 46 250 54 330 110 C250 78 120 68 0 84 Z"/>
    </svg>

    <div class="brand"><span class="brand-dot"></span>Larkmoor Law Group</div>
    <div class="brand-byline">by Attorney R. Calloway</div>

    <div class="contact">
      <div class="contact-line"><svg viewBox="0 0 10 10"><path d="M2 0 L4 2 L3 3.5 C4 5.5 4.5 6 6.5 7 L8 6 L10 8 L8.5 10 C4 9 1 6 0 1.5 Z"/></svg>404-731-2864</div>
      <div class="contact-line"><svg viewBox="0 0 10 10"><path d="M0 2 H10 V8 H0 Z M0 2 L5 6 L10 2"/></svg>info@larkmoorfirm.legal</div>
      <div class="contact-line"><svg viewBox="0 0 10 10"><circle cx="5" cy="5" r="5"/></svg>www.larkmoorfirm.legal</div>
      <div class="addresses">
        418 Halvern St., NW Suite #1500<br>
        Atlanta, Georgia 30308<br>
        5125 W. Tanner Rd. Douglasville, Georgia 30135
      </div>
    </div>

    <h1 class="salutation">Dear Mr. Ellis,</h1>

    <section class="letter-body">
      <p>Lorem Ipsum is simply dummy text of the printing and typesetting industry. Lorem Ipsum has been the industry's standard dummy text ever since the 1500s, when an unknown printer took a galley of type and scrambled it to make a type specimen book. It has survived not only five centuries, but also the leap into electronic typesetting, remaining essentially unchanged.</p>
      <p>The standard chunk of Lorem Ipsum used since the 1500s is reproduced below for those interested. Sections 1.10.32 and 1.10.33 from "de Finibus Bonorum et Malorum" by Corvinus are also reproduced in their exact original form, accompanied by English versions from the 1914 translation by H. Penwell</p>
      <p>Lorem Ipsum is simply dummy text of the printing and typesetting industry. Lorem Ipsum has been the industry's standard dummy text ever since the 1500s, when an unknown printer took a galley of type and scrambled it to make a type specimen book. It has survived not only five centuries, but also the leap into electronic typesetting, remaining essentially unchanged. It was popularised in the</p>
      <p>The standard chunk of Lorem Ipsum used since the 1500s is reproduced below for those interested. Sections 1.10.32 and 1.10.33 from "de Finibus Bonorum et Malorum" by Corvinus are also reproduced in their exact original form, accompanied by English versions from the 1914 translation by H. Penwell</p>
      <p>The standard chunk of Lorem Ipsum used since the 1500s is reproduced below for those interested. Sections 1.10.32 and 1.10.33 from "de Finibus Bonorum et Malorum" by Corvinus are</p>
    </section>

    <div class="signature" role="img" aria-label="Handwritten signature of the attorney"></div>
  </main>
</body>
</html>
```